Creation of a label for a sub brand of the Golden Comb Store and a logo for the label

We need a label to go on honey jars for a sub brand of the Golden Comb Store called Nectar Field Guy. This brand is up market and aimed at discerning consumers, foodies and raw honey connoisseurs. It may be available online as well as through delicatessens and up market supermarkets. We want the brand to built around Nectar Field Guy who goes out to seek the best quality raw monofloral honeys available. The label needs to show an image of me, with a friendly demeanour. See my response to a message that outlines more about the image.

Target Market(s)

Our target audience is upmarket consumers who appreciate high-quality products and are interested in the traceability of the product, organic production methods, and high bioactivity of the honey. They love raw honey and appreciate the different flavours available from a range of different plants and trees. They despise mass produced supermarket honey.

Industry/Entity Type

Artisan food

Requirements
Must have
• The image for Nectar Field Guy should probably be a photo, not a graphic likeness. You could use a substitute image for the moment but posed in a way that I could replicate.
Nice to have
• See the brief

```html
<!DOCTYPE html>
<html lang="en">
<head>
<meta charset="utf-8">
<title>Nectar Field Guy – Wild Lavender Label</title>
<link rel="stylesheet" href="https://fonts.googleapis.com/css2?family=Lilita+One&family=Cinzel:wght@400&family=Josefin+Sans:wght@300&family=Fira+Sans:wght@500&display=swap">
<style>
  :root {
    --canvas: #efede8;
    --gold: #d9a640;
    --gold-light: #e3b54e;
    --brown: #6e4219;
    --brown-deep: #3d2412;
    --ink: #3a2210;
    --lavender: #6b5aa8;
  }
  * { margin: 0; padding: 0; box-sizing: border-box; }
  html, body { width: 1200px; height: 1200px; overflow: hidden; }
  body {
    background: var(--canvas);
    display: flex; align-items: center; justify-content: center;
  }
  .label {
    position: relative;
    width: 936px; height: 890px;
    background: radial-gradient(ellipse 62% 70% at 50% 48%, var(--gold-light) 0%, var(--gold) 62%, #b17c2c 80%, var(--brown) 100%);
    overflow: hidden;
  }
  .badge {
    position: absolute;
    border-radius: 50%;
    border: 6px double var(--ink);
    display: flex; align-items: center; justify-content: center;
    text-align: center;
    color: var(--ink);
    font-family: "Fira Sans", sans-serif;
    font-weight: 500;
    background: var(--gold);
  }
  .badge--cert { left: 54px; top: 45px; width: 144px; height: 144px; }
  .badge--est { left: 738px; top: 45px; width: 144px; height: 144px; }
  .badge--weight { left: 62px; top: 684px; width: 124px; height: 124px; font-size: 38px; line-height: 0.9; }
  .badge--weight small { display: block; font-size: 26px; }
  .badge--origin { left: 752px; top: 680px; width: 124px; height: 124px; font-size: 20px; line-height: 1.05; }
  .portrait { position: absolute; left: 353px; top: 16px; width: 230px; height: 250px; }
  .brand-name {
    position: absolute; left: 0; right: 0; top: 274px;
    text-align: center;
    font-family: "Lilita One", sans-serif;
    font-size: 54px; line-height: 60px; color: var(--ink);
    letter-spacing: 1px;
    white-space: nowrap;
  }
  .product-type {
    position: absolute; left: 0; right: 0; top: 380px;
    text-align: center;
    font-family: "Josefin Sans", sans-serif; font-weight: 300;
    font-size: 58px; line-height: 66px; letter-spacing: 9px; color: var(--ink);
    white-space: nowrap;
  }
  .flavour-banner {
    position: absolute; left: 32px; right: 48px; top: 462px; height: 150px;
    background: var(--brown-deep);
    border-radius: 40px;
    display: flex; align-items: center; justify-content: center;
    font-family: "Cinzel", serif;
    font-size: 78px; line-height: 1; color: var(--gold);
    white-space: nowrap;
  }
  .features {
    position: absolute; left: 0; right: 0; top: 648px;
    list-style: none; text-align: center;
    font-family: "Fira Sans", sans-serif; font-weight: 500;
    font-size: 29px; line-height: 43px; color: var(--ink);
    white-space: nowrap;
  }
  .sprig { position: absolute; width: 40px; height: 140px; }
  .sprig--left { left: 12px; top: 672px; }
  .sprig--right { right: 12px; top: 668px; }
</style>
</head>
<body>
  <section class="label">
    <div class="badge badge--cert" role="img" aria-label="Organic certification badge"></div>
    <div class="badge badge--est" role="img" aria-label="Established badge"></div>

    <svg class="portrait" viewBox="0 0 230 250" role="img" aria-label="Photo of the beekeeper in a veiled hat inside a hexagon frame">
      <polygon points="115,4 226,66 226,184 115,246 4,184 4,66" fill="none" stroke="#3a2210" stroke-width="7"/>
      <polygon points="115,16 214,73 214,177 115,234 16,177 16,73" fill="#c8963a"/>
    </svg>

    <div class="brand-name">NECTAR FIELD GUY</div>
    <div class="product-type">ORGANIC RAW HONEY</div>
    <div class="flavour-banner">WILD LAVENDER</div>

    <ul class="features">
      <li>Cold-pressed | Unpasteurised</li>
      <li>Coarse-Filtered | 100% Raw</li>
      <li>Certified Organic | Wilderness Honey</li>
      <li>Artisan Beekeepers</li>
      <li>Unique Monofloral Honey</li>
    </ul>

    <div class="badge badge--weight"><span>500<small>gr.</small></span></div>
    <div class="badge badge--origin"><span>Country<br>of origin<br>SPAIN</span></div>

    <svg class="sprig sprig--left" viewBox="0 0 40 140" role="img" aria-label="Lavender sprig illustration">
      <rect x="4" y="0" width="32" height="140" rx="16" fill="#6b5aa8"/>
    </svg>
    <svg class="sprig sprig--right" viewBox="0 0 40 140" role="img" aria-label="Lavender sprig illustration">
      <rect x="4" y="0" width="32" height="140" rx="16" fill="#6b5aa8"/>
    </svg>
  </section>
</body>
</html>
```